Brinetide Yacht Management Full Page Ad Flyer

Yacht Management Package also includes the following periodic Monthly services:

Monthly full vessel systems checklist inspections
Diver For Hull Cleaning And Inspection Of Props, Shafts, and Zincs
Interior/Exterior Detailing and scheduled washdowns
Manage Haulout
Pump-out Services
On-call Captain and Crew Services
Updates

Need more time to provide more content to designers and the printing press template file.

Target Market(s)

Vessel owners, motor yachts, sailboats from 25 feet in length up to 125 feet in length. We do not do cruise ships or yachts larger than 125 feet. Someone who has their boat docked at their house or a local marina. We also offer mobile on-site services.

```html
<!DOCTYPE html>
<html lang="en">
<head>
<meta charset="utf-8">
<title>Brinetide Yacht Management – Flyer</title>
<link href="https://fonts.googleapis.com/css2?family=Syncopate:wght@400;700&family=Oswald:wght@300;500;700&family=Poppins:wght@400;600;700&display=swap" rel="stylesheet">
<style>
  :root{
    --page:#c4c4c4;
    --sea-deep:#062c35;
    --sea-mid:#0d5561;
    --sea-light:#1c8a96;
    --aqua:#2fd6e8;
    --aqua-soft:#5fe4f0;
    --ink:#ffffff;
    --badge:#0a1f24;
    --rule:rgba(255,255,255,.35);
  }
  *{margin:0;padding:0;box-sizing:border-box}
  html,body{width:1200px;height:851px;overflow:hidden;background:var(--page)}
  .flyer{
    position:absolute;left:286px;top:20px;width:627px;height:810px;overflow:hidden;
    color:var(--ink);font-family:'Oswald',sans-serif;
  }
  .sea-photo{
    position:absolute;inset:0;
    background:
      radial-gradient(ellipse 32% 55% at 80% 78%, rgba(150,215,220,.55), transparent 70%),
      radial-gradient(ellipse 55% 45% at 60% 45%, var(--sea-light), transparent 75%),
      linear-gradient(180deg, var(--sea-deep) 0%, var(--sea-mid) 45%, var(--sea-mid) 70%, var(--sea-deep) 100%);
  }
  .headline{position:absolute;left:0;top:0;width:627px;height:180px}
  .headline text{font-family:'Syncopate',sans-serif}
  .headline .big{font-weight:700;fill:var(--aqua)}
  .headline .sub{font-weight:400;fill:var(--ink)}

  .services{position:absolute;left:46px;top:205px;width:220px;list-style:none}
  .service{position:absolute;left:0;width:220px;display:flex;align-items:center}
  .service svg{width:38px;height:38px;flex:none;stroke:var(--aqua);fill:none;stroke-width:1.6}
  .service p{margin-left:14px;font-weight:300;font-size:15.5px;line-height:16px;text-transform:uppercase;letter-spacing:-.1px}
  .rule{position:absolute;left:46px;width:219px;border-top:1.5px dotted var(--rule)}

  .offer-badge{position:absolute;left:410px;top:220px;width:130px;height:130px;border-radius:50%;
    background:rgba(47,214,232,.25);display:flex;align-items:center;justify-content:center}
  .offer-badge .inner{width:112px;height:112px;border-radius:50%;background:var(--badge);
    display:flex;flex-direction:column;align-items:center;justify-content:center;text-align:center;font-family:'Poppins',sans-serif}
  .offer-badge .l1{font-size:15px;font-weight:600;line-height:15px}
  .offer-badge .l2{font-size:15px;font-weight:700;line-height:16px;color:var(--aqua)}
  .offer-badge .l3{font-size:10.5px;line-height:11px;margin-top:4px}

  .cta{position:absolute;left:49px;top:612px;font-family:'Poppins',sans-serif}
  .cta .lead{font-size:12.5px;line-height:14px}
  .cta .free{font-size:12.5px;line-height:14px;font-weight:700;color:var(--aqua)}
  .cta .phone{display:flex;align-items:center;margin-top:7px;font-size:19px;font-weight:700}
  .cta .phone svg{width:15px;height:15px;margin-right:4px;fill:none;stroke:var(--aqua);stroke-width:2}

  .haulout{position:absolute;left:237px;top:612px}
  .haulout .kicker{font-family:'Poppins',sans-serif;font-size:15px;letter-spacing:6px;color:var(--aqua);line-height:16px}
  .haulout .main{font-weight:700;font-size:38px;line-height:40px;letter-spacing:-.5px}

  .brand{position:absolute;left:48px;top:733px;font-family:'Poppins',sans-serif;font-size:17px;font-weight:400;letter-spacing:4px;line-height:20px}
  .divider{position:absolute;left:221px;top:720px;height:40px;border-left:1px solid var(--rule)}
  .locale{position:absolute;left:237px;top:718px;font-family:'Poppins',sans-serif}
  .locale .tag{font-size:6.5px;letter-spacing:1.6px;line-height:9px}
  .locale .area{display:flex;align-items:center;font-size:11px;font-weight:700;line-height:15px;margin-top:1px}
  .locale .area svg{width:8px;height:10px;margin-right:3px;fill:none;stroke:var(--aqua);stroke-width:2}
  .locale .web{font-size:10px;letter-spacing:1.3px;margin-top:5px}
</style>
</head>
<body>
<main class="flyer">
  <div class="sea-photo" role="img" aria-label="Aerial photo of a motor yacht cruising across turquoise sea, leaving a wide white wake"></div>

  <svg class="headline" viewBox="0 0 627 180" aria-label="Yacht Management – Periodic Monthly Services">
    <text class="big" x="45" y="91" font-size="52" textLength="244" lengthAdjust="spacingAndGlyphs">YACHT</text>
    <text class="big" x="45" y="138" font-size="52" textLength="538" lengthAdjust="spacingAndGlyphs">MANAGEMENT</text>
    <text class="sub" x="45" y="163" font-size="21" textLength="531" lengthAdjust="spacingAndGlyphs">PERIODIC MONTHLY SERVICES</text>
  </svg>

  <ul class="services">
    <li class="service" style="top:0">
      <svg viewBox="0 0 40 40"><path d="M6 26l3 7h22l3-7z"/><rect x="11" y="17" width="18" height="9"/><rect x="15" y="10" width="10" height="7"/><path d="M20 4v6M3 37q4-3 8 0t8 0 8 0 8 0"/></svg>
      <p>Monthly full vessel<br>systems checklist<br>inspections</p>
    </li>
    <li class="service" style="top:92px">
      <svg viewBox="0 0 40 40"><circle cx="20" cy="20" r="11"/><circle cx="20" cy="20" r="4"/><path d="M20 3v34M3 20h34M8 8l24 24M32 8L8 32"/></svg>
      <p>On-call captain &amp;<br>crew services</p>
    </li>
    <li class="service" style="top:163px">
      <svg viewBox="0 0 40 40"><rect x="5" y="20" width="30" height="10" rx="2"/><path d="M5 30v4M35 30v4M8 20v-4h24v4"/><rect x="24" y="6" width="9" height="7"/><path d="M9 16V8h4"/></svg>
      <p>Nterior/exterior<br>detailing &amp; scheduled<br>washdowns</p>
    </li>
    <li class="service" style="top:248px">
      <svg viewBox="0 0 40 40"><circle cx="20" cy="12" r="7"/><rect x="14" y="9" width="12" height="5" rx="2"/><path d="M8 36V26q0-6 6-6h12q6 0 6 6v10M20 20v16"/></svg>
      <p>Diver for hull cleaning<br>&amp; inspection of props,<br>shafts, and zincs</p>
    </li>
    <li class="service" style="top:331px">
      <svg viewBox="0 0 40 40"><rect x="4" y="12" width="18" height="16" rx="2"/><path d="M8 18v6M11 18v6M14 18v6M17 18v6M22 20h12M34 16v8M8 12V8h6v4"/></svg>
      <p>Pump-out services</p>
    </li>
  </ul>
  <div class="rule" style="top:279px"></div>
  <div class="rule" style="top:356px"></div>
  <div class="rule" style="top:439px"></div>
  <div class="rule" style="top:524px"></div>

  <div class="offer-badge">
    <div class="inner">
      <span class="l1">WE ALSO</span>
      <span class="l2">OFFER</span>
      <span class="l3">Mobile on-site<br>services</span>
    </div>
  </div>

  <div class="cta">
    <p class="lead">CALL TODAY FOR A</p>
    <p class="free">FREE ESTIMATE</p>
    <p class="phone"><svg viewBox="0 0 20 20"><circle cx="10" cy="10" r="8.5"/><path d="M7 6l2 2-1 1.5q1 2 2.5 2.5L12 11l2 2-1.5 1.5Q8 14 6 7.5z"/></svg>555 0142 7788</p>
  </div>

  <div class="haulout">
    <p class="kicker">MANAGE</p>
    <p class="main">HAULOUT</p>
  </div>

  <p class="brand">BRINETIDE</p>
  <div class="divider"></div>
  <div class="locale">
    <p class="tag">LOCATED IN</p>
    <p class="area"><svg viewBox="0 0 8 10"><path d="M4 9Q0.8 5 0.8 3.6a3.2 3.2 0 0 1 6.4 0Q7.2 5 4 9z"/></svg>SOUTH FLORIDA MIAMI AREA</p>
    <p class="web">www.brinetidemarine.com</p>
  </div>
</main>
</body>
</html>
```